Defense Attorney Business Card Design Project/ Stationary

I am looking for a distinctive business card design for my solo law practice.
I practice criminal defense, both juvenile and adult, including DUI. I am a very experienced attorney with prior military experience. The design should convey a traditional, old school flair, but not be too stodgy or uptight. Some color. My logo should appear.

Project Deadline Extended Reason: I misunderstood how this project works and I was not prepared with my logo when this project ran the first time. Added Thursday, November 13, 2014

Reason: I was sent overseas on military duty last year, which interrupted this project. Thank you for your participation... I hope we can get this done this week! Thank you, Des

Target Market(s)

Regular everyday people looking for strong, knowledgeable, authoritative representation while they are faced with criminal charges. Many have never been charged with a crime before. A reassuring air is therefore desired.

Industry/Entity Type

Business

Contact Information for Business Card

My information is:
Desmond R. Whitcombe, Attorney at Law
735 Linden Avenue Suite 300
Oakland, California 94618
Tel: (510) 555-0183
Fax: (510) 555-0162
email: deswhitcombelaw@mailbrook.net
web: www.deswhitcombelaw.net

Font styles to use
Serif
Sans Serif
Decorative

Colors
0255a3
ffffff

Requirements
Must have
• Sharp lines, bold elements. Conservative use of colors, such as deep blues, burgundy, grays for example.
• While my logo says "Des Whitcombe", it should be modified to show "Desmond R. Whitcombe".
Should not have
• Cliche imagery such as scales of justice, gavels, Tower of Varenholt, etc.

```html
<!DOCTYPE html>
<html lang="en">
<head>
<meta charset="utf-8">
<title>Desmond R. Whitcombe, Attorney At Law</title>
<link rel="stylesheet" href="https://fonts.googleapis.com/css2?family=Pathway+Gothic+One&family=Arimo:wght@400&display=swap">
<style>
  :root {
    --card-blue: #0a3ffa;
    --frame-black: #000000;
    --ink-white: #ffffff;
  }
  html, body {
    margin: 0;
    padding: 0;
    width: 1200px;
    height: 840px;
    overflow: hidden;
    background: var(--frame-black);
  }
  .business-card {
    display: block;
    width: 1200px;
    height: 840px;
  }
  .card-frame { fill: var(--frame-black); }
  .card-panel { fill: var(--card-blue); }
  .brand-name,
  .practice-title,
  .attorney-name {
    font-family: "Pathway Gothic One", "Arial Narrow", sans-serif;
    fill: var(--ink-white);
  }
  .brand-name { font-size: 168px; }
  .practice-title { font-size: 150px; }
  .attorney-name { font-size: 196px; }
  .contact-line {
    font-family: "Arimo", Arial, sans-serif;
    font-size: 37px;
    fill: var(--ink-white);
  }
  .contact-online { text-anchor: end; }
</style>
</head>
<body>
<svg class="business-card" viewBox="0 0 1200 840" xmlns="http://www.w3.org/2000/svg">
  <rect class="card-frame" x="0" y="0" width="1200" height="840"/>

  <g class="card-front">
    <rect class="card-panel" x="18" y="6" width="1164" height="508"/>
    <text class="brand-name" x="76" y="176" textLength="364" lengthAdjust="spacingAndGlyphs">Des Whitcombe</text>
    <text class="practice-title" x="308" y="302" textLength="586" lengthAdjust="spacingAndGlyphs">Attorney At Law</text>
    <text class="attorney-name" x="60" y="468" textLength="1004" lengthAdjust="spacingAndGlyphs">Desmond R. Whitcombe</text>
  </g>

  <g class="card-contact">
    <rect class="card-panel" x="18" y="524" width="1164" height="312"/>
    <text class="contact-line contact-address" x="54" y="582">735 Linden Avenue Suite 300</text>
    <text class="contact-line contact-address" x="54" y="630">Oakland, California</text>
    <text class="contact-line contact-online" x="1150" y="570">web www.deswhitcombelaw.net</text>
    <text class="contact-line contact-online" x="1176" y="630">email  deswhitcombelaw@mailbrook.net</text>
    <text class="contact-line contact-phone" x="64" y="756">(510) 555-0183</text>
    <text class="contact-line contact-phone" x="64" y="802">(510) 555-0162</text>
  </g>
</svg>
</body>
</html>
```